poster for the 2021 Tamarack Trial Circuit

A poster for our 2021 Tamarack Trial Circuit, featuring our dates of events and sponsors. 2017 example included. posters to be hung in various locations including but not limited too, gas stations, schools, business', restaurants. instructors are available. included different car shots from the track. these can be included or not up to the artist's discretion. celebrating over 50 years as a club.

Target Market(s)

auto enthusiasts and auto racing fans

Industry/Entity Type

Automotive

Font styles to use
Sans Serif

Colors
3377b5

Requirements
Must have
• dates for our events.

March 26-28 Vernal Marathon
April 17-18 Event 2-3
May 22-23 Event 4-5
June 12-13 Bramble Ridge HIllclimb
June 26-27 Event 6-7
July 31-August 1 Event 8-9
September 4-5 Event 10-11
October 2-3 Autumn Marathon

Sponsors pictures and cars as background
logo
"instructors are available"
the website, PKWRTALBOT.ORG
Nice to have
• clean design, understandable/ easy to ride and contrast.

```html
<!DOCTYPE html>
<html lang="en">
<head>
<meta charset="utf-8">
<title>2021 Tamarack Trial Circuit</title>
<link rel="stylesheet" href="https://fonts.googleapis.com/css2?family=Oswald:wght@300;400;500;600&family=Quicksand:wght@500;600&family=Tinos:ital,wght@0,400;1,700&display=swap">
<style>
:root{
  --navy:#050a18;
  --slate:#56687a;
  --brand-blue:#3377b5;
  --rust:#7a3b1e;
  --band:#b4652f;
  --amber:#f7941d;
  --orange:#f15a24;
  --white:#ffffff;
  --ink:#1d2a6b;
  --yellow:#f4e826;
}
*{margin:0;padding:0;box-sizing:border-box}
html,body{width:776px;height:1200px;overflow:hidden;background:var(--navy)}
.poster{position:relative;width:776px;height:1200px;overflow:hidden;background:var(--navy);font-family:"Quicksand",sans-serif}
.backdrop{position:absolute;inset:0;background:linear-gradient(180deg,#0a1426 0%,#0d2036 38%,#1e3550 58%,#4a5c6c 72%,var(--slate) 100%)}
.year{position:absolute;left:30px;top:26px;width:390px;height:230px;overflow:visible}
.year text{font-family:"Oswald",sans-serif;font-weight:400;font-size:288px;fill:var(--brand-blue)}
.title{position:absolute;left:444px;top:20px;width:300px;height:240px;overflow:visible}
.title text{font-family:"Oswald",sans-serif;font-weight:300;font-size:76px;fill:var(--brand-blue)}
.ribbon{position:absolute;left:625px;top:0;width:133px;height:158px}
.ribbon-text{position:absolute;left:625px;top:2px;width:133px;text-align:center;font-family:"Oswald",sans-serif;font-weight:600;color:var(--white);line-height:1}
.ribbon-text .small{display:block;font-size:23px;margin-top:4px}
.ribbon-text .big{font-size:50px;vertical-align:middle}
.ribbon-text .years{font-size:22px;vertical-align:middle}
.schedule{position:absolute;left:7px;top:296px;width:570px;height:440px;background:rgba(0,0,0,.86);padding:24px 0 0 18px}
.schedule ul{list-style:none}
.schedule li{font-size:29px;font-weight:500;line-height:35px;color:var(--white);white-space:nowrap}
.schedule .gap{height:35px}
.schedule .feature{color:var(--amber)}
.schedule .event{color:var(--orange)}
.instructors{position:absolute;left:608px;top:622px;width:160px;height:70px;overflow:visible}
.instructors text{font-family:"Oswald",sans-serif;font-weight:500;font-size:26px;fill:var(--orange)}
.diagonals{position:absolute;left:0;top:640px}
.club-mark{position:absolute;left:452px;top:985px;width:100px;height:100px}
.club-name{position:absolute;left:565px;top:990px;width:200px;font-family:"Quicksand",sans-serif;font-weight:600;font-size:18px;line-height:23px;color:var(--white);white-space:nowrap}
.sponsors{position:absolute;left:0;top:1127px;height:73px;width:776px}
.sponsor{position:absolute;top:0;height:73px;overflow:hidden}
.sponsor-hale{left:0;width:167px;background:var(--white);display:flex;align-items:center;justify-content:center}
.sponsor-hale span{font-family:"Quicksand",sans-serif;font-weight:600;font-size:20px;color:var(--ink);white-space:nowrap}
.sponsor-market{left:170px;width:138px;background:var(--yellow);border:2px solid #222;text-align:center;color:#111;font-weight:600}
.sponsor-market .name{display:block;font-size:14px;line-height:16px;margin-top:8px}
.sponsor-market .addr{display:block;font-size:8.5px;line-height:10px;margin-top:12px}
.sponsor-notary{left:312px;width:134px;background:#f4efe6;font-family:"Tinos",serif;color:#222;padding:4px 4px}
.sponsor-notary .name{font-style:italic;font-weight:700;font-size:8px;display:block}
.sponsor-notary .role{font-size:5px;display:block;margin-bottom:12px}
.sponsor-notary .detail{font-size:5.4px;line-height:6.6px;display:block;width:82px}
.sponsor-notary .quill{position:absolute;right:6px;top:6px;width:40px;height:60px;background:linear-gradient(160deg,#d9d3c7,#4a4540);border-radius:4px}
.sponsor-notary .fine{position:absolute;right:2px;bottom:3px;font-size:3px;width:22px;line-height:3.6px}
.sponsor-juniper{left:448px;width:64px;background:var(--white);display:flex;align-items:center;justify-content:center;text-align:center}
.sponsor-juniper span{font-weight:600;font-size:13px;line-height:15px;color:#111}
.website{position:absolute;left:525px;top:1148px;font-weight:500;font-size:26px;color:var(--orange);letter-spacing:.5px;white-space:nowrap}
</style>
</head>
<body>
<main class="poster">
  <div class="backdrop" role="img" aria-label="Toned photograph of an old town street with storefronts, fading into a track surface"></div>

  <svg class="year" viewBox="0 0 390 230" aria-label="2021">
    <text x="0" y="226" textLength="385" lengthAdjust="spacingAndGlyphs">2021</text>
  </svg>
  <svg class="title" viewBox="0 0 300 240" role="heading" aria-level="1" aria-label="Tamarack Trial Circuit">
    <text x="0" y="72" textLength="172" lengthAdjust="spacingAndGlyphs">TAMARACK</text>
    <text x="0" y="151" textLength="150" lengthAdjust="spacingAndGlyphs">TRIAL</text>
    <text x="0" y="230" textLength="262" lengthAdjust="spacingAndGlyphs">CIRCUIT</text>
  </svg>

  <svg class="ribbon" viewBox="0 0 133 158" aria-hidden="true">
    <polygon points="0,0 133,0 133,158 66,128 0,158" fill="var(--rust)"/>
  </svg>
  <div class="ribbon-text">
    <span class="small">CELEBRATING</span>
    <span class="small">MORE THAN</span>
    <span class="big">50</span> <span class="years">YEARS!</span>
  </div>

  <section class="schedule">
    <ul>
      <li><span class="feature">VERNAL MARATHON</span> February 27-28</li>
      <li><span class="event">EVENT #2-3</span> March 26-28</li>
      <li><span class="event">EVENT #4-5</span> April 17-18</li>
      <li><span class="event">EVENT #6-7</span> May 22-23</li>
      <li class="gap"></li>
      <li><span class="feature">BRAMBLE RIDGE HILLCLIMB</span> June 12-13</li>
      <li><span class="event">Event #8-9</span> June 26-27</li>
      <li><span class="event">EVENT #10-11</span> July 31-August 1</li>
      <li><span class="event">EVENT #12-13</span> September 4-5</li>
      <li class="gap"></li>
      <li><span class="feature">AUTUMN MARATHON</span> October 2-3</li>
    </ul>
  </section>

  <svg class="instructors" viewBox="0 0 160 70" aria-label="Instructors are available!">
    <text x="0" y="26" textLength="157" lengthAdjust="spacingAndGlyphs">INSTRUCTORS ARE</text>
    <text x="0" y="62" textLength="98" lengthAdjust="spacingAndGlyphs">AVAILABLE!</text>
  </svg>

  <svg class="diagonals" width="776" height="480" viewBox="0 0 776 480" aria-hidden="true">
    <polygon points="0,210 776,30 776,70 0,248" fill="var(--band)" opacity=".85"/>
    <polygon points="0,400 776,180 776,230 0,445" fill="var(--band)" opacity=".75"/>
    <g role="img" aria-label="Track photographs: a blue classic coupe, a black and gold muscle car and an orange modern coupe cornering between cones">
      <polygon points="0,255 233,201 233,370 0,420" fill="#8a8f94"/>
      <polygon points="235,200 520,135 520,300 235,370" fill="#9a9ea2"/>
      <polygon points="522,134 776,76 776,172 522,300" fill="#a9adb0"/>
    </g>
  </svg>

  <svg class="club-mark" viewBox="0 0 100 100" aria-hidden="true">
    <circle cx="50" cy="50" r="44" fill="none" stroke="var(--white)" stroke-width="4"/>
  </svg>
  <p class="club-name">PARKWRIGHT<br>TALBOT<br>CAR CLUB<br>ALDER, OREGON</p>

  <footer class="sponsors">
    <div class="sponsor sponsor-hale"><span>Hale Insurance</span></div>
    <div class="sponsor sponsor-market">
      <span class="name">QUICK STOP<br>MARKET</span>
      <span class="addr">214 Oak Ave. Alder, OR 97000<br>555-014-2290</span>
    </div>
    <div class="sponsor sponsor-notary">
      <span class="name">Dana R. Whitlow</span>
      <span class="role">Mobile Notary • Certified Signing Agent</span>
      <span class="detail">Serving Southern Oregon<br>Licensed &amp; Insured<br>Available Anytime<br>555-013-7781<br>whitlownotary@mail.example</span>
      <div class="quill" role="img" aria-label="Quill pen and ink bottle"></div>
      <span class="fine">Not an attorney; no legal advice given</span>
    </div>
    <div class="sponsor sponsor-juniper"><span>JUNIPER<br>17</span></div>
  </footer>
  <p class="website">PKWRTALBOT.ORG</p>
</main>
</body>
</html>
```